PELMARK
stationery items
Professional
Karim Doulani
Managing Director
Corniva Plaza L27
Al Fannar Road
P.O. Box 58214
Dubai - UAE
kdoulani@pelmark-gulfa.com
www.pelmark-gulfa.com
looking for full stationery items (business cards, letter heads, envelopes)
LOGO
Strategy Think-tank & Real Estate Asset Management Solutions
full package of logo

```html
<!DOCTYPE html>
<html lang="en">
<head>
<meta charset="utf-8">
<title>Pelmark Stationery</title>
<link href="https://fonts.googleapis.com/css2?family=Cormorant+Garamond:wght@500;600&display=swap" rel="stylesheet">
<style>
  :root{
    --backdrop:#a9a9a9;
    --paper:#ffffff;
    --edge:#cfcfcf;
    --brand:#7b2a30;
    --ink:#3a3a3a;
    --muted:#6d6d6d;
    --fold:#bdbdbd;
  }
  *{margin:0;padding:0;box-sizing:border-box}
  html,body{width:1200px;height:684px;overflow:hidden;background:var(--backdrop)}
  body{position:relative;font-family:"Cormorant Garamond",Georgia,serif;color:var(--ink)}
  .sheet{position:absolute;background:var(--paper);border:1px solid var(--edge)}
  .brand{font-family:"Cormorant Garamond",Georgia,serif;font-weight:600;color:var(--brand);letter-spacing:.06em;white-space:nowrap;position:absolute}
  .small{position:absolute;font-size:7px;line-height:9px;color:var(--muted);white-space:nowrap}

  /* letterhead */
  .letterhead{left:149px;top:12px;width:439px;height:665px}
  .letterhead .brand{left:14px;top:26px;font-size:22px}
  .letterhead .web{right:14px;top:14px}
  .letterhead .footer{left:14px;bottom:14px}

  /* business cards */
  .card{width:192px;height:125px;border-radius:8px}
  .card-front-a{left:12px;top:223px}
  .card-front-b{left:216px;top:223px}
  .card .brand{left:14px;top:38px;font-size:20px}
  .card .tagline{left:14px;top:92px;font-size:6.5px}
  .card-back{width:192px;height:130px;border-radius:2px}
  .card-back-a{left:12px;top:355px}
  .card-back-b{left:216px;top:355px}
  .card-back .brand{left:10px;top:14px;font-size:15px}
  .card-back .person{right:10px;top:14px;text-align:right}
  .person .name{font-size:9px;font-weight:600;color:var(--ink);line-height:10px}
  .person .role{font-size:6.5px;color:var(--muted);line-height:8px}
  .card-back .contact{left:10px;top:72px}

  /* envelopes */
  .envelope-back{left:636px;top:228px;width:552px;height:151px;overflow:hidden}
  .envelope-back svg{position:absolute;left:0;top:0}
  .envelope-back .brand{left:50%;transform:translateX(-50%);top:70px;font-size:22px}
  .envelope-back .web{right:12px;bottom:8px}
  .envelope-front{left:636px;top:384px;width:552px;height:288px}
  .envelope-front .brand{left:22px;top:40px;font-size:22px}
  .envelope-front .web{right:14px;top:14px}
  .envelope-front .contact{left:22px;top:196px}
</style>
</head>
<body>

<section class="sheet letterhead">
  <div class="small web">www.pelmark-gulfa.com</div>
  <div class="brand">PELMARK</div>
  <div class="small footer">
    kdoulani@pelmark-gulfa.com<br>
    T +971 4 382 5100 &nbsp; F +971 4 382 5101<br>
    Corniva Plaza L27, Al Fannar Road, P.O. Box 58214, Dubai - UAE
  </div>
</section>

<section class="sheet card card-front-a">
  <div class="brand">PELMARK</div>
  <div class="small tagline">Strategy Think-tank &amp; Real Estate Asset Management Solutions</div>
</section>
<section class="sheet card card-front-b">
  <div class="brand">PELMARK</div>
  <div class="small tagline">Strategy Think-tank &amp; Real Estate Asset Management Solutions</div>
</section>

<section class="sheet card-back card-back-a">
  <div class="brand">PELMARK</div>
  <div class="person" style="position:absolute">
    <div class="name">Karim Doulani</div>
    <div class="role">Managing Director</div>
  </div>
  <div class="small contact">
    kdoulani@pelmark-gulfa.com<br>
    T +971 4 382 5100<br>
    M +971 50 614 2278<br>
    Corniva Plaza L27, Al Fannar Road, P.O. Box 58214, Dubai - UAE
  </div>
</section>
<section class="sheet card-back card-back-b">
  <div class="brand">PELMARK</div>
  <div class="person" style="position:absolute">
    <div class="name">Karim Doulani</div>
    <div class="role">Managing Director</div>
  </div>
</section>

<section class="sheet envelope-back">
  <svg width="552" height="151" viewBox="0 0 552 151" aria-hidden="true">
    <path d="M0 0 Q150 40 276 58 Q402 40 552 0" fill="none" stroke="var(--fold)" stroke-width="1"/>
  </svg>
  <div class="brand">PELMARK</div>
  <div class="small web">www.pelmark-gulfa.com</div>
</section>

<section class="sheet envelope-front">
  <div class="small web">www.pelmark-gulfa.com</div>
  <div class="brand">PELMARK</div>
  <div class="small contact">
    kdoulani@pelmark-gulfa.com<br>
    T +971 4 382 5100 &nbsp; F +971 4 382 5101<br>
    Corniva Plaza L27, Al Fannar Road, P.O. Box 58214, Dubai - UAE
  </div>
</section>

</body>
</html>
```